File Download Website

We are looking for a design for a file download website. Our objective is to allow users to upload/browse/download files. This means we need 3 different pages.
The upload page should allow users to upload a file, we are looking for creative designs, a file box with a browse button next to it is already out there so the design must bring something new.
The browse page should display a users files/folders.
The download page should allow the user to download a file.
We do not require any code, only design. The designer is given complete freedom over the design, you may go about it however you like. This is a test of creativity, whoever this project goes to will definitely be given more work in the near future.
Example of a well designed file download website: cloudvane.net
Target Market(s)
15-30 year old people
Industry/Entity Type
Work
Look and feel
Each slider illustrates characteristics of the customer's brand and the style your logo design should communicate.

```html
<!DOCTYPE html>
<html lang="en">
<head>
<meta charset="utf-8">
<title>Stashly – My Files</title>
<link rel="stylesheet" href="https://fonts.googleapis.com/css2?family=Open+Sans:ital,wght@0,400;0,600;0,700;1,400&display=swap">
<style>
:root{
  --brand:#0b8fd9;
  --brand-dark:#0a74b8;
  --brand-light:#86d3f6;
  --slate:#4f6070;
  --row:#e8f0f5;
  --line:#d5dadf;
  --text:#444c55;
  --muted:#8b9299;
  --faint:#a9afb5;
  --footer:#f0f1f2;
  --white:#ffffff;
  --folder:#f2c53d;
  --icon:#5fb3df;
}
*{box-sizing:border-box;margin:0;padding:0}
html,body{width:1200px;height:953px;overflow:hidden;background:var(--white)}
body{font-family:"Open Sans",Arial,sans-serif;color:var(--text)}
.stage{position:relative;width:980px;height:778px;transform:scale(1.22449);transform-origin:0 0}
.abs{position:absolute}

/* header */
.topbar{left:0;top:0;width:980px;height:56px;background:var(--brand)}
.brand{left:25px;top:12px;display:flex;align-items:center;gap:10px;color:var(--white);font-weight:700;font-size:25px;letter-spacing:.3px}
.brand-dot{width:26px;height:26px;border-radius:50%;background:var(--white)}
.view-switch{left:269px;top:7px;width:126px;height:43px;border-radius:7px;background:var(--brand-light);padding:4px 5px;display:flex;gap:4px}
.view-btn{width:56px;height:35px;border-radius:5px;background:linear-gradient(#1590d3,var(--brand-dark));display:flex;align-items:center;justify-content:center}
.search{left:407px;top:10px;width:336px;height:37px;border-radius:7px;background:var(--white);overflow:hidden;display:flex}
.search-type{width:95px;height:100%;background:linear-gradient(#e6e8ea,#c9cdd1);font-size:12px;font-weight:700;color:#3d4650;display:flex;align-items:center;justify-content:center;gap:4px}
.search-field{flex:1;padding-left:10px;font-size:14px;color:#555;display:flex;align-items:center}
.search-icon{width:38px;display:flex;align-items:center;justify-content:center}
.nav{left:762px;top:21px;font-size:12px;color:var(--white);display:flex;gap:16px}

/* sub header */
.pathbar{left:0;top:56px;width:980px;height:38px;background:var(--slate);color:var(--white);font-size:14px;display:flex;align-items:center;padding-left:31px;gap:8px}

/* sidebar tree */
.sidebar{left:0;top:94px;width:181px;height:348px;border-right:1px solid #b9bec3}
.tree-item{position:absolute;display:flex;align-items:center;font-size:12px;color:#6a7179}
.tree-item.root{color:#333a41;font-weight:700}
.caret{position:absolute;font-size:8px;color:var(--brand)}

/* file table */
.table-head{left:203px;top:100px;width:773px;height:26px;border-bottom:1px solid #c9ced3}
.col-sep{position:absolute;top:0;width:1px;height:24px;background:var(--line)}
.head-name{left:42px;top:5px;font-size:12px;font-weight:700;color:#3a4a5a}
.head-mod{left:525px;top:3px;font-size:12px;color:var(--faint)}
.checkbox{position:absolute;width:13px;height:13px;border:1px solid #c6cbd0;border-radius:2px;background:#f7f8f9}
.row{position:absolute;left:203px;width:776px;height:39px;background:var(--row)}
.row .cell-sep{position:absolute;top:0;width:1px;height:39px;background:var(--white)}
.row .name{position:absolute;left:85px;top:9px;font-size:15px;color:var(--text);white-space:nowrap}
.row .meta{font-size:11px;font-style:italic;color:var(--muted);margin-left:6px}
.row .date{position:absolute;left:532px;top:11px;font-size:12.5px;color:var(--faint)}
.row svg{position:absolute;left:46px;top:6px}

/* footer */
.statusbar{left:0;top:442px;width:980px;height:47px;background:var(--footer);border-top:2px solid #e2e4e6}
.status-text{left:82px;top:8px;font-size:14px;color:var(--muted)}
</style>
</head>
<body>
<svg width="0" height="0" style="position:absolute">
  <defs>
    <symbol id="folder-screen" viewBox="0 0 28 26">
      <rect x="1" y="2" width="26" height="18" rx="2" fill="var(--icon)"/>
      <rect x="3" y="4" width="22" height="14" fill="#d6ecf8"/>
      <path d="M6 7h5l1.5 2H22v7H6z" fill="var(--icon)"/>
      <rect x="12" y="20" width="4" height="3" fill="var(--icon)"/>
      <rect x="8" y="23" width="12" height="2" fill="var(--icon)"/>
    </symbol>
  </defs>
</svg>

<div class="stage">
  <header class="abs topbar"></header>
  <div class="abs brand"><span class="brand-dot"></span>Stashly</div>

  <div class="abs view-switch">
    <div class="view-btn">
      <svg width="24" height="22" viewBox="0 0 24 22"><rect x="2" y="3" width="20" height="13" rx="1.5" fill="none" stroke="#fff" stroke-width="2"/><path d="M12 5l-4 4h3v4h2V9h3z" fill="#fff"/><rect x="8" y="18" width="8" height="2" fill="#fff"/></svg>
    </div>
    <div class="view-btn">
      <svg width="26" height="22" viewBox="0 0 26 22"><rect x="2" y="2" width="22" height="14" rx="1.5" fill="none" stroke="#fff" stroke-width="2"/><path d="M7 6h5l1 1.5h6V13H7z" fill="#fff"/><rect x="9" y="18" width="8" height="2" fill="#fff"/></svg>
    </div>
  </div>

  <div class="abs search">
    <div class="search-type">all types <span>▼</span></div>
    <div class="search-field">Search</div>
    <div class="search-icon">
      <svg width="18" height="18" viewBox="0 0 18 18"><circle cx="7" cy="7" r="5.5" fill="none" stroke="#9aa1a8" stroke-width="2"/><path d="M11 11l5.5 5.5" stroke="#9aa1a8" stroke-width="2.5" stroke-linecap="round"/></svg>
    </div>
  </div>

  <nav class="abs nav"><span>My Files</span><span>|</span><span>Settings</span><span>|</span><span>Log Out</span></nav>

  <div class="abs pathbar">
    <svg width="22" height="20"><use href="#folder-screen" style="--icon:#ffffff"/></svg>
    My Files
  </div>

  <aside class="abs sidebar">
    <span class="caret" style="left:13px;top:22px">▼</span>
    <div class="tree-item root" style="left:26px;top:16px"><svg width="21" height="20" style="margin-right:7px"><use href="#folder-screen" style="--icon:#0b8fd9"/></svg>My Files</div>
    <div class="tree-item" style="left:36px;top:46px"><svg width="21" height="20" style="margin-right:7px"><use href="#folder-screen"/></svg>Documents</div>
    <span class="caret" style="left:24px;top:77px">▶</span>
    <div class="tree-item" style="left:36px;top:71px"><svg width="21" height="20" style="margin-right:7px"><use href="#folder-screen"/></svg>Music</div>
    <span class="caret" style="left:24px;top:102px">▶</span>
    <div class="tree-item" style="left:36px;top:96px"><svg width="21" height="20" style="margin-right:7px"><use href="#folder-screen"/></svg>Photos</div>
    <span class="caret" style="left:24px;top:127px">▶</span>
    <div class="tree-item" style="left:36px;top:121px"><svg width="21" height="20" style="margin-right:7px"><use href="#folder-screen"/></svg>Videos</div>
  </aside>

  <div class="abs table-head">
    <span class="checkbox" style="left:11px;top:6px"></span>
    <span class="col-sep" style="left:35px"></span>
    <span class="abs head-name">NAME <span style="color:#8d949b">▲</span></span>
    <span class="col-sep" style="left:516px"></span>
    <span class="abs head-mod">MODIFIED</span>
  </div>

  <div class="row" style="top:127px">
    <span class="checkbox" style="left:11px;top:12px"></span><span class="cell-sep" style="left:35px"></span>
    <svg width="29" height="27"><use href="#folder-screen"/></svg>
    <span class="name">Documents<span class="meta">Folders: 0, Files: 0</span></span>
    <span class="cell-sep" style="left:516px"></span><span class="date">2013-06-21 08:43:16</span>
  </div>
  <div class="row" style="top:167px">
    <span class="checkbox" style="left:11px;top:12px"></span><span class="cell-sep" style="left:35px"></span>
    <svg width="29" height="27"><use href="#folder-screen"/></svg>
    <span class="name">Music<span class="meta">Folders: 0, Files: 0</span></span>
    <span class="cell-sep" style="left:516px"></span><span class="date">2013-06-21 08:43:16</span>
  </div>
  <div class="row" style="top:207px">
    <span class="checkbox" style="left:11px;top:12px"></span><span class="cell-sep" style="left:35px"></span>
    <svg width="29" height="27"><use href="#folder-screen"/></svg>
    <span class="name">Photos<span class="meta">Folders: 0, Files: 0</span></span>
    <span class="cell-sep" style="left:516px"></span><span class="date">2013-06-21 08:43:16</span>
  </div>
  <div class="row" style="top:247px">
    <span class="checkbox" style="left:11px;top:12px"></span><span class="cell-sep" style="left:35px"></span>
    <svg width="29" height="27"><use href="#folder-screen"/></svg>
    <span class="name">Videos<span class="meta">Folders: 0, Files: 0</span></span>
    <span class="cell-sep" style="left:516px"></span><span class="date">2013-06-21 08:43:16</span>
  </div>

  <footer class="abs statusbar">
    <svg class="abs" style="left:34px;top:7px" width="37" height="34" viewBox="0 0 28 26">
      <rect x="1" y="2" width="26" height="18" rx="2" fill="#5fb3df"/>
      <rect x="3" y="4" width="22" height="14" fill="#d6ecf8"/>
      <path d="M6 7h5l1.5 2H22v7H6z" fill="var(--folder)"/>
      <rect x="12" y="20" width="4" height="3" fill="#5fb3df"/>
      <rect x="8" y="23" width="12" height="2" fill="#5fb3df"/>
    </svg>
    <span class="abs status-text">4 Items</span>
  </footer>
</div>
</body>
</html>
```